Gutschein-Design zur Pflegeberatung
Zielgruppe
Wir feiern mit unserem Pflegedienst das 10 Jährige Jubiläum. Da es wegen der Corona Pandemie keine Feierlichkeiten geben kann, würde ich wir einen Gutschein für eine kostenlose Pflegeberatung erstellen lassen. Auf die Vorderseite bitte den Gutschein mit dem Text:
Bilder bitte aus den öffentlichen Portalen verwenden.
Gutschein zur Pflegeberatung
Wir unterstützen bei der Beantragung eines Pflegegrades und helfen bei abgelehnten Anträgen.
Gerne informieren wir Sie über umfangreiche Möglichkeiten der ambulante Pflege und erstellen einen individuellen Versorgungsplan. Darüber hinaus erhalte Sie praktische Tipps zu Alltagshilfen und konkrete Hilfestellungen rund um die Pflege, damit Sie noch so lange wie möglich zu
Hause bleiben können.
Unten bitte einfügen: Gutschein gültig bis einschließlich Juli 2022
Auf die Rückseite bitte eine kurze Info zu unserem 10 Jährigen bestehen.
Vielleicht vielleicht wieder mit dem Slogan, Seit 10 Jahren rund um die Uhr für Sie im Einsatz.
Aufgabenstellung
Da wir zwei ambulante Filialen betreiben, muss das Logo auf die zweite Filiale angepasst werden.
Der Text und die Informationen bleiben jedoch gleich. Der Gutschein sollte sofort auffallen und animieren, im Pflegedienst anzurufen.

```html
<!DOCTYPE html>
<html lang="de">
<head>
<meta charset="utf-8">
<title>Gutschein Pflegeberatung – Pflegeteam Hafenlicht</title>
<link href="https://fonts.googleapis.com/css2?family=Nunito:wght@400;600;700;800;900&display=swap" rel="stylesheet">
<style>
  :root{
    --green:#3aaa45;
    --blue:#1d4e96;
    --orange:#ec7f22;
    --white:#ffffff;
    --ink:#1f1f1f;
    --bg:#efefef;
    --photo-warm-a:#f3e6d8;
    --photo-warm-b:#3f86c9;
    --photo-cool-a:#e9ecef;
    --photo-cool-b:#b9c9da;
  }
  *{box-sizing:border-box;margin:0;padding:0}
  html,body{width:1200px;height:800px;overflow:hidden;background:var(--bg);font-family:"Nunito",sans-serif}
  .canvas{position:relative;width:1200px;height:800px}
  .card{position:absolute;left:210px;width:780px;height:360px;background:var(--white);overflow:hidden;box-shadow:0 6px 18px rgba(0,0,0,.18)}
  .card--front{top:24px}
  .card--back{top:412px}

  /* front */
  .hero-photo{position:absolute;left:0;top:0;width:470px;height:250px;
    background:linear-gradient(100deg,var(--photo-warm-a) 0%,#eadbcb 45%,var(--photo-warm-b) 85%)}
  .brand{position:absolute;left:22px;top:20px;display:flex;align-items:center;gap:10px}
  .brand__dot{width:44px;height:44px;border-radius:50%;background:var(--green)}
  .brand__name{color:var(--green);font-weight:800;font-size:19px;line-height:1.05;width:130px}
  .voucher-panel{position:absolute;left:470px;top:0;width:310px;height:250px;background:var(--green);color:var(--white);text-align:center;padding-top:30px}
  .voucher-panel__title{font-weight:900;font-size:50px;line-height:1}
  .voucher-panel__sub{font-weight:700;font-size:17px;margin-top:2px}
  .voucher-panel__valid-label{font-size:13px;font-weight:600;margin-top:22px}
  .voucher-panel__valid{display:inline-block;background:var(--white);color:var(--green);font-weight:700;font-size:15px;line-height:1.2;padding:6px 18px;margin-top:6px}
  .web-tab{position:absolute;right:40px;top:222px;background:var(--orange);color:var(--white);font-size:12px;font-weight:700;padding:5px 12px;border-radius:6px 6px 0 0;white-space:nowrap}
  .info-band{position:absolute;left:0;top:250px;width:780px;height:110px;background:var(--blue);border-top:4px solid var(--orange);color:var(--white);padding:14px 100px 0 26px;font-size:13px;line-height:1.45;font-weight:600}
  .info-band__arrow{position:absolute;right:28px;top:24px;width:40px;height:40px}

  /* back */
  .jubilee{position:absolute;left:26px;top:20px;width:505px}
  .jubilee__headline{color:var(--green);font-weight:800;font-size:31px;line-height:1.15}
  .jubilee__headline strong{font-weight:900}
  .jubilee__quote{color:var(--ink);font-size:14px;line-height:1.5;margin-top:12px}
  .jubilee__call{color:var(--ink);font-size:14px;line-height:1.5;margin-top:12px}
  .jubilee__phone{color:var(--green);font-weight:800;font-size:19px}
  .photo{position:absolute;left:545px;width:235px}
  .photo--top{top:0;height:152px;background:linear-gradient(135deg,var(--photo-cool-a),var(--photo-cool-b))}
  .photo--bottom{top:160px;height:160px;background:linear-gradient(135deg,#f2f4f6,#9db7d6)}
  .contact-bar{position:absolute;left:0;bottom:0;width:780px;height:40px;display:flex;color:var(--white);font-weight:700;font-size:14px;white-space:nowrap}
  .contact-bar__item{display:flex;align-items:center;padding:0 18px}
  .contact-bar__address{background:var(--green);width:300px}
  .contact-bar__mail{background:var(--blue);width:245px}
  .contact-bar__web{background:var(--orange);width:235px;justify-content:center;padding:0 8px;font-size:13px}
</style>
</head>
<body>
<div class="canvas">

  <section class="card card--front" aria-label="Vorderseite Gutschein">
    <div class="hero-photo" role="img" aria-label="Foto: Pflegerin in blauer Kleidung lächelt mit einer älteren Dame"></div>
    <div class="brand">
      <span class="brand__dot"></span>
      <span class="brand__name">Pflegeteam Hafenlicht</span>
    </div>
    <div class="voucher-panel">
      <div class="voucher-panel__title">Gutschein</div>
      <div class="voucher-panel__sub">zur Pflegeberatung</div>
      <div class="voucher-panel__valid-label">gültig bis :</div>
      <div class="voucher-panel__valid">einschließlich<br>Juli 2022</div>
    </div>
    <div class="web-tab">www.pflegeteam-hafenlicht.de</div>
    <div class="info-band">
      Wir unterstützen bei der Beantragung eines Pflegegrades und helfen bei abgelehnten Anträgen. Gerne informieren wir Sie über umfangreiche Möglichkeiten der ambulante Pflege und erstellen einen individuellen Versorgungsplan. Darüber hinaus erhalte Sie praktische Tipps zu Alltagshilfen und konkrete Hilfestellungen rund um die Pflege, damit Sie noch so lange wie möglich zu Hause bleiben können.
      <svg class="info-band__arrow" viewBox="0 0 40 40" aria-hidden="true">
        <path d="M6 36 C8 20 16 14 28 13" fill="none" stroke="#fff" stroke-width="4" stroke-linecap="round"/>
        <path d="M24 5 L35 13 L24 21 Z" fill="#fff"/>
      </svg>
    </div>
  </section>

  <section class="card card--back" aria-label="Rückseite Jubiläum">
    <div class="jubilee">
      <h2 class="jubilee__headline">Seit <strong>10 Jahren</strong> rund um die<br>Uhr für Sie im Einsatz.</h2>
      <p class="jubilee__quote">"Wir vom <strong>Pflegeteam Hafenlicht</strong> sind ein Team dem die Individualität eines jeden Stärke verleiht und uns so das Selbstverständnis im Umgang mit der Einzigartigkeit jedes Patienten lehrt. Unser ambulanter Pflegedienst bietet Ihnen mit seinem Team erfahrener und motivierter Mitarbeiter ein Höchstmaß an Wohlbefinden und Eigenständigkeit sowie eine Entlastung Ihrer Angehörigen."</p>
      <p class="jubilee__call">Wir sind für Sie da und freuen uns auf ein persönliches Kennenlernen. Rufen Sie uns unter <span class="jubilee__phone">0800 246 80 13</span> an.</p>
    </div>
    <div class="photo photo--top" role="img" aria-label="Foto: Pflegerin hilft einer älteren Dame beim Zuknöpfen der Bluse"></div>
    <div class="photo photo--bottom" role="img" aria-label="Foto: Beraterin bespricht Unterlagen mit einem älteren Ehepaar"></div>
    <div class="contact-bar">
      <div class="contact-bar__item contact-bar__address">Lindenweg 12 24680 Seestadt</div>
      <div class="contact-bar__item contact-bar__mail">info@pflegeteam-hafenlicht.de</div>
      <div class="contact-bar__item contact-bar__web">www.pflegeteam-hafenlicht.de</div>
    </div>
  </section>

</div>
</body>
</html>
```